Harbor Nest Lodging website, brand new company, that rents rooms out in houses to milleniuls

We have a site right now that is weak as heck! We could use some punching it up. So we want it to be fun and cool, with added items in for social media (just chirpnet now) and anything else you want to throw at us. We do have a “blog” in there dedicated to events (we throw a lot of them) so want to incorporate that. Also have an existing design for a hand out that we want to use as our launching pad for colors… you can deviate from it a bit though.

Target Market(s)

25-40 year olds transitioning to the city from other places in the country. Millennial are the min group

Industry/Entity Type

Real Estate

Coding

Coded - Design and coding required

Number of Pages Required

5+ page

Font styles to use
Sans Serif

Requirements
Must have
• Fun look, same pages as those uploaded, but not necessarily the look and feel of what we have already.
• Follow the content of our posted site www.HarborNestLodging.example
• FOOTER
• LOGO | SITEMAP | SOCIAL LINKS | MAIN CTA REMINDER | CONTACT INFO | COPYRIGHT INFO | TERMS AND CONDITIONS
Nice to have
• Use as many of my graphics as loaded, but feel free to use stock photos as well interlaced. Including both people in their 20’s, 30’s, 40’s, having a fun time or of nice houses, inside and out.

```html
<!DOCTYPE html>
<html lang="en">
<head>
<meta charset="utf-8">
<title>Harbor Nest Lodging</title>
<link href="https://fonts.googleapis.com/css2?family=Oswald:wght@300;400;500&family=Open+Sans:wght@400;600;700&display=swap" rel="stylesheet">
<style>
:root{
  --navy:#16325f;
  --blue:#1f6db5;
  --blue-light:#3f8fd6;
  --orange:#f29a1f;
  --text:#555b63;
  --muted:#8a9099;
  --line:#d5d9de;
  --footer:#eef0f2;
  --white:#ffffff;
}
*{box-sizing:border-box;margin:0;padding:0}
html,body{width:880px;height:1200px;overflow:hidden;background:var(--white);font-family:"Open Sans",Arial,sans-serif;color:var(--text)}
.page{position:relative;width:880px;height:1200px}

.topbar{height:26px;background:var(--navy);display:flex;justify-content:flex-end;align-items:center;gap:28px;padding-right:36px;font-size:11px;color:var(--white)}
.topbar span{display:flex;align-items:center;gap:6px;white-space:nowrap}
.topbar .phone{font-weight:700;font-size:13px}

.header{height:72px;display:flex;align-items:center;justify-content:space-between;padding:0 34px 0 70px}
.brand{display:flex;align-items:center;gap:8px;font-family:"Oswald",sans-serif;font-weight:500;font-size:20px;color:var(--navy);letter-spacing:1px;text-transform:uppercase;white-space:nowrap}
.brand-dot{width:12px;height:12px;border-radius:50%;background:var(--blue)}
.nav{display:flex;gap:12px;font-size:10px;text-transform:uppercase;color:var(--text);align-items:center;white-space:nowrap}
.nav .active{border:1px solid var(--blue);padding:4px 8px;color:var(--blue)}

.hero{position:relative;height:400px;background:linear-gradient(120deg,#d7d2cb 0%,#e8e2da 30%,#c9b9a4 60%,#8f7b66 100%)}
.hero-title{position:absolute;left:70px;top:100px;font-family:"Oswald",sans-serif;font-weight:500;font-size:38px;line-height:42px;color:var(--white);text-transform:uppercase;text-shadow:0 2px 4px rgba(0,0,0,.25)}
.hero-title em{font-style:normal;color:var(--orange)}
.circles{position:absolute;left:70px;right:70px;bottom:-24px;display:flex;justify-content:space-between;align-items:flex-end}
.circle{width:80px;height:80px;border-radius:50%;border:3px solid var(--white);background:radial-gradient(circle at 40% 35%,#b59a80,#5d4a3e)}
.circle.big{width:112px;height:112px;background:radial-gradient(circle at 40% 35%,#d8c29f,#8a6a4c)}

.info{display:flex;gap:50px;padding:70px 70px 0}
.col{flex:1}
.mark-slot{width:46px;height:10px;margin-bottom:6px;background:var(--line)}
.section-title{font-family:"Oswald",sans-serif;font-weight:300;font-size:27px;text-transform:uppercase;color:var(--blue);letter-spacing:.5px;margin-bottom:22px;border-top:1px solid var(--line);padding-top:6px;white-space:nowrap}
.section-title em{font-style:normal;color:var(--orange)}
.field{width:310px;height:24px;border:1px solid var(--line);margin-bottom:12px;font-size:10px;padding:5px 8px;color:var(--muted)}
.field.message{height:88px}
.submit{display:inline-block;background:var(--blue);color:var(--white);font-size:11px;font-weight:700;padding:6px 14px}
.lead{font-size:10px;margin:-10px 0 10px}
.map{height:130px;background:linear-gradient(135deg,#e4e6e2,#d6dbd4);border:1px solid var(--line);margin-bottom:16px}
.contact-row{display:flex;align-items:flex-start;gap:10px;font-size:10px;margin-bottom:10px;line-height:14px}
.contact-row strong{color:var(--blue)}
.ico{flex:none}

.footer{position:absolute;left:0;right:0;top:990px;height:188px;background:var(--footer);padding:22px 70px;display:flex;gap:40px;overflow:hidden}
.footer h4{font-size:11px;font-weight:700;color:var(--navy);text-transform:uppercase;margin-bottom:8px}
.footer ul{list-style:none;font-size:9px;line-height:14px}
.footer .details{font-size:9px;line-height:13px}
.footer .details p{display:flex;gap:6px;align-items:center;margin-bottom:6px}
.map-round{width:130px;height:130px;border-radius:50%;background:linear-gradient(135deg,#e3e6e0,#c9d1c8);border:3px solid var(--white);margin-top:10px;flex:none}
.follow{margin-left:auto;text-align:right;position:relative;width:200px;z-index:2}
.socials{display:flex;gap:6px;justify-content:flex-end}
.social{width:20px;height:20px;background:var(--blue)}
.social.alt{background:var(--navy)}
.social.warm{background:#c0392b}
.swoosh{position:absolute;right:0;bottom:0;width:420px;height:120px}
.footer-brand{position:absolute;right:60px;bottom:14px;font-family:"Oswald",sans-serif;font-weight:500;font-size:20px;color:var(--white);text-transform:uppercase;letter-spacing:1px;white-space:nowrap}
.copyright{position:absolute;left:0;right:0;bottom:0;height:22px;background:var(--navy);color:var(--white);font-size:8px;padding:6px 70px}
</style>
</head>
<body>
<div class="page">
  <div class="topbar">
    <span><svg width="12" height="9" viewBox="0 0 12 9"><rect x=".5" y=".5" width="11" height="8" fill="none" stroke="#fff"/><path d="M.5 .5 6 5l5.5-4.5" fill="none" stroke="#fff"/></svg>info@harbornestlodging.example</span>
    <span class="phone"><svg width="11" height="11" viewBox="0 0 24 24"><path fill="#fff" d="M6.6 10.8a15 15 0 0 0 6.6 6.6l2.2-2.2a1 1 0 0 1 1-.25 11.4 11.4 0 0 0 3.6.6 1 1 0 0 1 1 1V20a1 1 0 0 1-1 1A17 17 0 0 1 3 4a1 1 0 0 1 1-1h3.5a1 1 0 0 1 1 1c0 1.25.2 2.45.6 3.6a1 1 0 0 1-.25 1z"/></svg>555-014-2290</span>
  </div>

  <header class="header">
    <div class="brand"><span class="brand-dot"></span>Harbor Nest Lodging</div>
    <nav class="nav">
      <span>Home</span><span>About Us</span><span>Our Communities</span><span>Amenities</span><span>Fitting</span><span>Events</span><span>Investors</span><span class="active">Contact</span>
    </nav>
  </header>

  <section class="hero" role="img" aria-label="Photo of a group of smiling young adults giving thumbs up in a bright living room">
    <h1 class="hero-title">See<br>What's<br><em>Available...</em></h1>
    <div class="circles">
      <div class="circle" role="img" aria-label="Photo of residents at a party"></div>
      <div class="circle" role="img" aria-label="Photo of friends gathering"></div>
      <div class="circle big" role="img" aria-label="Photo of a group event outdoors"></div>
      <div class="circle" role="img" aria-label="Photo of a shared kitchen"></div>
      <div class="circle" role="img" aria-label="Photo of residents relaxing"></div>
      <div class="circle" role="img" aria-label="Photo of a house interior"></div>
    </div>
  </section>

  <section class="info">
    <div class="col">
      <div class="mark-slot" role="img" aria-label="Small brand mark"></div>
      <h2 class="section-title">Schedule Viewing <em>Today!</em></h2>
      <div class="field">First Name</div>
      <div class="field">Last Name</div>
      <div class="field">Email</div>
      <div class="field">Phone</div>
      <div class="field message">Message</div>
      <span class="submit">SUBMIT</span>
    </div>
    <div class="col">
      <div class="mark-slot" role="img" aria-label="Small brand mark"></div>
      <h2 class="section-title">Harbor Nest <em>Lodging</em></h2>
      <p class="lead">Saving money is just a nice perk</p>
      <div class="map" role="img" aria-label="Street map showing the office location"></div>
      <div class="contact-row"><svg class="ico" width="14" height="14" viewBox="0 0 24 24"><path fill="#1f6db5" d="M12 2a7 7 0 0 0-7 7c0 5 7 13 7 13s7-8 7-13a7 7 0 0 0-7-7zm0 9.5A2.5 2.5 0 1 1 12 6.5a2.5 2.5 0 0 1 0 5z"/></svg><div><strong>HARBOR NEST LODGING</strong><br>PO Box 4410, Harborview, ST 00001</div></div>
      <div class="contact-row"><svg class="ico" width="14" height="14" viewBox="0 0 24 24"><path fill="#1f6db5" d="M6.6 10.8a15 15 0 0 0 6.6 6.6l2.2-2.2a1 1 0 0 1 1-.25 11.4 11.4 0 0 0 3.6.6 1 1 0 0 1 1 1V20a1 1 0 0 1-1 1A17 17 0 0 1 3 4a1 1 0 0 1 1-1h3.5a1 1 0 0 1 1 1c0 1.25.2 2.45.6 3.6a1 1 0 0 1-.25 1z"/></svg><div>555-014-2290</div></div>
      <div class="contact-row"><svg class="ico" width="14" height="14" viewBox="0 0 24 24"><rect x="2" y="5" width="20" height="14" fill="none" stroke="#1f6db5" stroke-width="2"/><path d="M2 5l10 8 10-8" fill="none" stroke="#1f6db5" stroke-width="2"/></svg><div>info@harbornestlodging.example</div></div>
    </div>
  </section>

  <footer class="footer">
    <div>
      <h4>Quick Links</h4>
      <ul><li>HOME</li><li>ABOUT US</li><li>OUR COMMUNITIES</li><li>AMENITIES</li><li>FITTING</li><li>EVENTS</li><li>CONTACT US</li></ul>
    </div>
    <div class="details">
      <h4>Contact Details</h4>
      <p><span><strong>HARBOR NEST LODGING</strong><br>PO Box 4410<br>Harborview, ST 00001</span></p>
      <p>☏ 555-014-2290</p>
      <p>☏ 555-014-2291</p>
      <p>✉ info@harbornestlodging.example</p>
    </div>
    <div class="map-round" role="img" aria-label="Round street map of the neighborhood"></div>
    <div class="follow">
      <h4>Follow Us</h4>
      <div class="socials"><span class="social alt"></span><span class="social"></span><span class="social"></span><span class="social warm"></span><span class="social"></span></div>
    </div>
    <svg class="swoosh" viewBox="0 0 420 120" preserveAspectRatio="none"><path d="M0 120 C90 80 220 50 420 36 V120 Z" fill="#1f6db5"/><path d="M0 120 C100 88 230 62 420 52" fill="none" stroke="#3f8fd6" stroke-width="3"/></svg>
    <div class="footer-brand">Harbor Nest Lodging</div>
  </footer>
  <div class="copyright">Copyright © 2016 HARBOR NEST LODGING. All Rights Reserved.</div>
</div>
</body>
</html>
```